Veltarum

Standard Business Card design.
Sample two-sided design uploaded. White front, Black back.
Would like white shield to be on all black background side.
Willing to look at a couple creative designs, but nothing crazy.
Preference for a classic, confident, strong design.

```html
<!DOCTYPE html>
<html lang="en">
<head>
<meta charset="utf-8">
<title>Veltarum Business Card</title>
<link href="https://fonts.googleapis.com/css2?family=PT+Sans+Narrow:wght@400;700&display=swap" rel="stylesheet">
<style>
  :root {
    --page: #ffffff;
    --ink: #111111;
    --card-dark: #000000;
    --card-light: #ffffff;
    --on-dark: #faf8f8;
    --trim: #c8c8c8;
  }
  html, body {
    margin: 0;
    padding: 0;
    width: 1200px;
    height: 928px;
    overflow: hidden;
    background: var(--page);
  }
  .sheet {
    position: relative;
    width: 1200px;
    height: 928px;
    font-family: "PT Sans Narrow", "Arial Narrow", sans-serif;
    color: var(--ink);
  }
  .card {
    position: absolute;
    width: 390px;
    box-sizing: border-box;
  }
  .card--back {
    left: 191px;
    top: 129px;
    height: 606px;
    background: var(--card-dark);
    display: flex;
    align-items: center;
    justify-content: center;
  }
  .back-name {
    color: var(--on-dark);
    font-weight: 700;
    font-size: 64px;
    letter-spacing: 4px;
    text-transform: uppercase;
    margin-top: -70px;
  }
  .card--front {
    left: 615px;
    top: 134px;
    height: 602px;
    background: var(--card-light);
    border: 1px solid var(--trim);
    text-align: center;
  }
  .person {
    position: absolute;
    top: 46px;
    left: 0;
    right: 0;
  }
  .person__name {
    font-weight: 700;
    font-size: 23px;
    line-height: 30px;
  }
  .person__role {
    font-weight: 400;
    font-size: 22px;
    line-height: 30px;
  }
  .brand {
    position: absolute;
    top: 395px;
    left: 0;
    right: 0;
    font-weight: 700;
    font-size: 40px;
    letter-spacing: 5px;
    text-transform: uppercase;
  }
  .contact {
    position: absolute;
    top: 500px;
    left: 0;
    right: 0;
    font-size: 22px;
    line-height: 25px;
  }
  .contact p { margin: 0; }
</style>
</head>
<body>
<div class="sheet">
  <section class="card card--back" aria-label="Card back">
    <div class="back-name">Veltarum</div>
  </section>

  <section class="card card--front" aria-label="Card front">
    <div class="person">
      <div class="person__name">Name Surname</div>
      <div class="person__role">Executive Director</div>
    </div>
    <div class="brand">Veltarum</div>
    <div class="contact">
      <p>T. 1234 555 0190</p>
      <p>hello@veltarum.com</p>
      <p>www.veltarum.com</p>
    </div>
  </section>
</div>
</body>
</html>
```